New Business Card Design For Re-Branded Company (New Logo)

We recently switched our DBA and had a new logo designed. We now need new business cards made around our new logo. We would like to stick with the color scheme in our logo: White, Orange, and Blue. We want to see original bold designs that reflect our position in the solar energy sector but we prefer simple over complicated.

We are curious about vertical designs so if you can translate your design onto a vertical layout we would be open to look at it. We especially like a few designs we have seen on here that are vertical with a black or very dark gray background. They have our logo on one side and then the normal vertical business card on the other side.

I have included a screenshot of one of the samples we like, labeled sample.jpg and a file we were given as an example of our logo on a dark background.

At the same time we are satisfied to stay with what we have always had in a horizontal format. If it's not a lot of extra work for you, designs that are submitted in both horizontal and vertical formats will be greatly appreciated.

Please submit your original, bold, clean designs for consideration. Contact us with any questions or comments that may arise.

Thank you and Good Luck,

RT

```html
<!DOCTYPE html>
<html lang="en">
<head>
<meta charset="utf-8">
<title>Radiant Tide — Business Card</title>
<link rel="stylesheet" href="https://fonts.googleapis.com/css2?family=Montserrat:wght@400;500;600&display=swap">
<style>
  :root {
    --backdrop: #e9e6e1;
    --card: #1f2022;
    --card-edge: #2a2b2e;
    --orange: #f5822a;
    --blue: #2a8bd6;
    --white: #f2f2f2;
  }
  * { box-sizing: border-box; margin: 0; padding: 0; }
  html, body { width: 1200px; height: 843px; overflow: hidden; }
  body {
    background: var(--backdrop);
    font-family: "Montserrat", sans-serif;
    position: relative;
  }
  .card {
    position: absolute;
    top: 267px;
    width: 540px;
    height: 309px;
    background: var(--card);
    border: 1px solid var(--card-edge);
    box-shadow: 0 14px 30px rgba(0,0,0,0.25);
    overflow: hidden;
  }
  .card--back { left: 40px; }
  .card--front { left: 620px; }

  /* back side: brand centred */
  .brand-lockup {
    position: absolute;
    inset: 0;
    display: flex;
    flex-direction: column;
    align-items: center;
    justify-content: center;
    gap: 14px;
  }
  .brand-dot {
    width: 42px; height: 42px;
    border: 4px solid var(--orange);
    border-radius: 50%;
  }
  .brand-name {
    font-weight: 600;
    font-size: 30px;
    letter-spacing: 1px;
    color: var(--orange);
  }

  /* front side */
  .accent-ring {
    position: absolute;
    left: -70px; top: 10px;
    width: 290px; height: 290px;
    border: 16px solid var(--orange);
    border-radius: 50%;
  }
  .holder {
    position: absolute;
    right: 30px; top: 34px;
    text-align: right;
  }
  .holder-name {
    font-weight: 600;
    font-size: 19px;
    letter-spacing: 1.5px;
    color: var(--blue);
  }
  .holder-title {
    font-weight: 500;
    font-size: 12px;
    letter-spacing: 1px;
    color: var(--orange);
    margin-top: 4px;
  }
  .contact {
    position: absolute;
    right: 30px; top: 108px;
    list-style: none;
    text-align: right;
    color: var(--white);
    font-size: 13px;
    line-height: 20px;
  }
  .contact li { display: flex; justify-content: flex-end; align-items: center; gap: 10px; }
  .contact .icon { width: 13px; height: 13px; flex: none; }
  .contact .icon--blank { visibility: hidden; }
  .address { margin-bottom: 6px; }
  .front-brand {
    position: absolute;
    right: 30px; bottom: 22px;
    font-weight: 600;
    font-size: 28px;
    letter-spacing: 1px;
    color: var(--blue);
  }
</style>
</head>
<body>

  <section class="card card--back" aria-label="Card back">
    <div class="brand-lockup">
      <span class="brand-dot" aria-hidden="true"></span>
      <span class="brand-name">RADIANT TIDE</span>
    </div>
  </section>

  <section class="card card--front" aria-label="Card front">
    <span class="accent-ring" aria-hidden="true"></span>

    <div class="holder">
      <p class="holder-name">MARA QUILL</p>
      <p class="holder-title">CEO/FOUNDER</p>
    </div>

    <ul class="contact">
      <li class="address">142 Larchwood Road<br>Fairbanks, Alaska 99701</li>
      <li>907 555 0148
        <svg class="icon" viewBox="0 0 16 16" aria-hidden="true"><path fill="#2a8bd6" d="M3 1h3l1.5 4-2 1.3a9 9 0 0 0 4.2 4.2L11 8.5l4 1.5v3a2 2 0 0 1-2 2A12 12 0 0 1 1 3a2 2 0 0 1 2-2z"/></svg>
      </li>
      <li>907 555 0172
        <svg class="icon" viewBox="0 0 16 16" aria-hidden="true"><rect x="4" y="1" width="8" height="14" rx="1.5" fill="none" stroke="#2a8bd6" stroke-width="1.6"/><circle cx="8" cy="12.5" r="0.9" fill="#2a8bd6"/></svg>
      </li>
      <li>907 555 0196
        <svg class="icon" viewBox="0 0 16 16" aria-hidden="true"><rect x="4" y="1" width="8" height="4" fill="#f5822a"/><rect x="1" y="5" width="14" height="7" rx="1" fill="#f5822a"/><rect x="4" y="10" width="8" height="5" fill="#f2f2f2"/></svg>
      </li>
      <li>hello@radianttide.com
        <svg class="icon" viewBox="0 0 16 16" aria-hidden="true"><rect x="1" y="3" width="14" height="10" rx="1" fill="#2a8bd6"/><path d="M1.5 4 8 9l6.5-5" fill="none" stroke="#1f2022" stroke-width="1.3"/></svg>
      </li>
      <li>www.radianttide.com
        <svg class="icon" viewBox="0 0 16 16" aria-hidden="true"><circle cx="8" cy="8" r="6.5" fill="none" stroke="#2a8bd6" stroke-width="1.5"/><ellipse cx="8" cy="8" rx="2.8" ry="6.5" fill="none" stroke="#2a8bd6" stroke-width="1.2"/><path d="M1.5 8h13" stroke="#2a8bd6" stroke-width="1.2"/></svg>
      </li>
    </ul>

    <p class="front-brand">RADIANT TIDE</p>
  </section>

</body>
</html>
```